Verdant Loop Advisors, LLC

I am looking for a simple, clear layout with my logo prominent and embossed, on the best quality card stock available. I would like the business name and phone number included on the card as well......I dont want my name anywhere on the card and I would like my logo embossed on the card......something simple with a white back......open to designs as long as they go along with recycling symbols and green type stuff.....The address, website, cell number, fax number, and email are listed below

5374 Tillbury Fenwood Road
Corbin Falls, MD 20999

c. 240.555.0143 f. 240.555.0187
e. sales@verdantloopadvisors.example
w. www.verdantloopadvisors.example

Industry/Entity Type

Recycling

```html
<!DOCTYPE html>
<html lang="en">
<head>
<meta charset="utf-8">
<title>Verdant Loop Advisors, LLC — Business Card</title>
<link href="https://fonts.googleapis.com/css2?family=Open+Sans:wght@400;800&display=swap" rel="stylesheet">
<style>
  :root {
    --backdrop: #7efcaa;
    --card-green: #0b6a2e;
    --brand-green: #0f7a34;
    --card-white: #ffffff;
    --ink: #1c1c1c;
    --shadow: rgba(0, 60, 25, 0.28);
  }
  * { box-sizing: border-box; margin: 0; padding: 0; }
  html, body {
    width: 1200px;
    height: 900px;
    overflow: hidden;
  }
  body {
    background: var(--backdrop);
    font-family: "Open Sans", Arial, sans-serif;
    display: flex;
    align-items: center;
    justify-content: center;
    gap: 48px;
  }
  .card {
    width: 525px;
    height: 300px;
    border-radius: 4px;
    box-shadow: 0 14px 30px var(--shadow);
    position: relative;
    overflow: hidden;
  }

  /* Front: green face with the brand name */
  .card-front {
    background: var(--card-green);
    display: flex;
    align-items: center;
    justify-content: center;
    gap: 20px;
    padding: 0 36px;
  }
  .front-mark {
    width: 64px;
    height: 64px;
    border-radius: 50%;
    background: var(--card-white);
    flex: none;
  }
  .front-name {
    color: var(--card-white);
    font-weight: 800;
    font-size: 30px;
    line-height: 1.1;
    letter-spacing: 0.5px;
    text-transform: uppercase;
  }

  /* Back: white face with contact details */
  .card-back {
    background: var(--card-white);
    padding: 40px 44px;
    display: flex;
    flex-direction: column;
    justify-content: center;
    gap: 30px;
  }
  .back-name {
    color: var(--brand-green);
    font-weight: 800;
    font-size: 24px;
    letter-spacing: 0.5px;
    text-transform: uppercase;
  }
  .contact-list {
    list-style: none;
    display: flex;
    flex-direction: column;
    gap: 7px;
    color: var(--ink);
    font-size: 14.5px;
    font-weight: 400;
  }
  .contact-item {
    display: flex;
    align-items: flex-start;
    gap: 10px;
    line-height: 1.3;
  }
  .contact-icon {
    width: 14px;
    height: 14px;
    flex: none;
    margin-top: 2px;
    fill: var(--brand-green);
  }
</style>
</head>
<body>

  <section class="card card-front" aria-label="Card front">
    <span class="front-mark" aria-hidden="true"></span>
    <p class="front-name">Verdant Loop Advisors, LLC</p>
  </section>

  <section class="card card-back" aria-label="Card back">
    <p class="back-name">Verdant Loop Advisors, LLC</p>
    <ul class="contact-list">
      <li class="contact-item">
        <svg class="contact-icon" viewBox="0 0 16 16" aria-hidden="true"><path d="M3.6 1.2l2.3 2.9-1.4 1.6c.9 2 2.6 3.7 4.6 4.6l1.6-1.4 2.9 2.3-1.3 2.5C7 13.5 2.5 9 1.1 3.7z"/></svg>
        <span>240.555.0143</span>
      </li>
      <li class="contact-item">
        <svg class="contact-icon" viewBox="0 0 16 16" aria-hidden="true"><path d="M4 1h6l2 2v3H4zM1 7h14v6h-2v2H3v-2H1zm4 3v3h6v-3z"/></svg>
        <span>240.555.0187</span>
      </li>
      <li class="contact-item">
        <svg class="contact-icon" viewBox="0 0 16 16" aria-hidden="true"><path d="M1 3h14v10H1zm1.5 1.5V5l5.5 4 5.5-4v-.5z"/></svg>
        <span>sales@verdantloopadvisors.example</span>
      </li>
      <li class="contact-item">
        <svg class="contact-icon" viewBox="0 0 16 16" aria-hidden="true"><path d="M8 1a7 7 0 110 14A7 7 0 018 1zm0 2a5 5 0 100 10A5 5 0 008 3z"/><path d="M3 7.3h10v1.4H3z"/><path d="M7.3 2h1.4v12H7.3z"/></svg>
        <span>www.verdantloopadvisors.example</span>
      </li>
      <li class="contact-item">
        <svg class="contact-icon" viewBox="0 0 16 16" aria-hidden="true"><path d="M8 1l7 6.5h-2V15H9.5v-4h-3v4H3V7.5H1z"/></svg>
        <span>5374 Tillbury Fenwood Road<br>Corbin Falls, MD 20999</span>
      </li>
    </ul>
  </section>

</body>
</html>
```